church business card design

we have a logo and would like our business card to complement the logo. we would prefer the logo in white on a coloured background - probably blue. Under the logo or near it we would have the Words 'Love God. Love people. Follow Jesus.'
We would like some yellow/gold highlights. We like the design by mintaro quill 4821 front of card - https://www.pelvarostudio.com/businesscard-design/contest/5812094

Our church is multicultural, inner city, friendly, warm welcoming and that's the feel we would like. there's also an element of being spontaneous, so a swirl or swoosh might help give that feel. the example card above had some curved shapes on the front of the card for example.
on the second side of the card would have the details of the Senior Pastor and the contact details for the church.
after the business card we would be looking at letterhead and an A5 flyer for printing but also as document templates so we can create invitations etc going forward

```html
<!DOCTYPE html>
<html lang="en">
<head>
<meta charset="utf-8">
<title>Keystone Church – Business Card</title>
<link href="https://fonts.googleapis.com/css2?family=Oswald:wght@600&family=Saira:wght@400;500&display=swap" rel="stylesheet">
<style>
  :root {
    --backdrop: #0c1026;
    --card-navy: #172052;
    --card-navy-deep: #121a44;
    --gold: #d4a21e;
    --gold-soft: #b8923a;
    --text-light: #e8eaf2;
    --relief: #1d2760;
  }
  * { margin: 0; padding: 0; box-sizing: border-box; }
  html, body {
    width: 1200px; height: 800px; overflow: hidden;
    background: var(--backdrop);
  }
  .stage { position: relative; width: 1200px; height: 800px; }
  .card {
    position: absolute; top: 136px;
    width: 302px; height: 526px;
    background: linear-gradient(180deg, var(--card-navy) 0%, var(--card-navy-deep) 100%);
    font-family: "Saira", sans-serif;
    color: var(--text-light);
  }
  .card--contact { left: 288px; }
  .card--brand { left: 630px; }

  .contact-frame {
    position: absolute; inset: 15px;
    border: 2px solid var(--gold-soft);
  }
  .contact-body {
    position: absolute; left: 0; right: 0; top: 160px;
    text-align: center;
  }
  .pastor-name {
    font-family: "Oswald", sans-serif; font-weight: 600;
    font-size: 31px; line-height: 1; color: var(--gold);
    letter-spacing: 0.5px;
  }
  .pastor-role { font-size: 17px; margin-top: 4px; }
  .address { font-size: 15px; line-height: 20px; margin-top: 12px; }
  .icon-row {
    display: flex; align-items: center; justify-content: center;
    gap: 6px; margin: 16px 0 12px;
  }
  .icon-row .rule { width: 46px; height: 1px; background: var(--text-light); margin: 0 4px; }
  .icon-row svg { display: block; }
  .contact-lines { font-size: 15px; line-height: 20px; }

  .brand-block {
    position: absolute; left: 56px; top: 40px; width: 200px;
  }
  .brand-name {
    font-size: 30px; font-weight: 500; line-height: 1.05;
    color: var(--gold); letter-spacing: 1px;
  }
  .brand-rule { height: 1px; background: var(--gold-soft); margin: 10px 0 3px; }
  .tagline { font-size: 11.5px; color: var(--gold); white-space: nowrap; }
  .relief-area {
    position: absolute; left: 58px; top: 194px;
    width: 216px; height: 332px;
    background: radial-gradient(ellipse at 50% 45%, var(--relief) 0%, rgba(29,39,96,0) 70%);
  }
</style>
</head>
<body>
<main class="stage">
  <section class="card card--contact">
    <div class="contact-frame"></div>
    <div class="contact-body">
      <h1 class="pastor-name">DANIEL HARGROVE</h1>
      <p class="pastor-role">Senior Pastor</p>
      <p class="address">4120 Birchwood Court<br>Fairbanks, Alaska 99712</p>
      <div class="icon-row">
        <span class="rule"></span>
        <svg width="17" height="17" viewBox="0 0 17 17" aria-label="phone">
          <rect width="17" height="17" rx="2" fill="var(--gold)"/>
          <path d="M5 3.5l2 2.2-1 1.3c.7 1.5 1.8 2.6 3.3 3.3l1.3-1 2.2 2-1 1.6C8 12.5 4.5 9 3.8 4.6z" fill="var(--card-navy)"/>
        </svg>
        <svg width="17" height="17" viewBox="0 0 17 17" aria-label="email">
          <rect width="17" height="17" rx="2" fill="var(--gold)"/>
          <rect x="3.5" y="5" width="10" height="7" fill="none" stroke="var(--card-navy)" stroke-width="1.3"/>
          <path d="M3.5 5l5 4 5-4" fill="none" stroke="var(--card-navy)" stroke-width="1.3"/>
        </svg>
        <svg width="17" height="17" viewBox="0 0 17 17" aria-label="website">
          <rect width="17" height="17" rx="2" fill="var(--gold)"/>
          <circle cx="8.5" cy="8.5" r="5" fill="none" stroke="var(--card-navy)" stroke-width="1.3"/>
          <ellipse cx="8.5" cy="8.5" rx="2" ry="5" fill="none" stroke="var(--card-navy)" stroke-width="1.1"/>
          <path d="M3.5 8.5h10" stroke="var(--card-navy)" stroke-width="1.1"/>
        </svg>
        <span class="rule"></span>
      </div>
      <p class="contact-lines">907-418-2263<br>pastor@keystonechurch.org<br>keystonechurch.org</p>
    </div>
  </section>

  <section class="card card--brand">
    <div class="brand-block">
      <p class="brand-name">Keystone<br>Church</p>
      <div class="brand-rule"></div>
      <p class="tagline">Love God • Love people • Follow Jesus</p>
    </div>
    <div class="relief-area" role="img" aria-label="Blind-embossed church emblem decoration"></div>
  </section>
</main>
</body>
</html>
```